Bref créative
Norland Equity Partners
Investing
Professional
Tom Radcliffe
President
728 Maplewood Ave. Suite 310
Oak Terrace, CA 90418
tom@NorlandEquityPartners.com
www.NorlandEquityPartners.com
We want our logo to be the main component of the card. Have fun and let me see what you got!
Feel free to try 1 or 2 sided card ideas.
Can use other fonts besides the logo font if you desire.

```html
<!DOCTYPE html>
<html lang="en">
<head>
<meta charset="utf-8">
<title>Norland Equity Partners – Business Cards</title>
<link href="https://fonts.googleapis.com/css2?family=Montserrat:wght@400;600;700;800&display=swap" rel="stylesheet">
<style>
  :root {
    --bg: #8d8c87;
    --card: #ffffff;
    --red: #e3262b;
    --ink: #1d1d1d;
    --grey: #6b6b6b;
  }
  * { box-sizing: border-box; margin: 0; padding: 0; }
  html, body { width: 1200px; height: 932px; overflow: hidden; }
  body {
    background: var(--bg);
    font-family: "Montserrat", Arial, sans-serif;
    position: relative;
  }
  .card {
    position: absolute;
    width: 500px;
    height: 290px;
    background: var(--card);
    border-radius: 26px;
    overflow: hidden;
    box-shadow: 0 10px 24px rgba(0,0,0,.35);
  }
  .card--front { left: 100px; top: 190px; }
  .card--back  { left: 600px; top: 450px; }

  .brand {
    position: absolute;
    left: 0; right: 0; top: 46px;
    display: flex; flex-direction: column; align-items: center;
  }
  .brand__row { display: flex; align-items: center; gap: 12px; }
  .brand__dot { width: 38px; height: 38px; border-radius: 50%; background: var(--red); }
  .brand__name {
    font-weight: 700; color: var(--ink);
    font-size: 28px; letter-spacing: 1px; line-height: 1;
  }
  .brand__tag {
    margin-top: 10px;
    display: flex; align-items: center; gap: 10px;
    font-weight: 700; color: var(--ink);
    font-size: 12px; letter-spacing: 5px;
  }
  .brand__tag::before, .brand__tag::after {
    content: ""; width: 54px; height: 1.5px; background: var(--ink);
  }

  .person {
    position: absolute; left: 0; right: 0; top: 150px; text-align: center;
  }
  .person__name { color: var(--red); font-weight: 800; font-size: 17px; letter-spacing: 1px; }
  .person__title { color: var(--grey); font-size: 10px; margin-top: 3px; }

  .contact {
    position: absolute; left: 60px; right: 40px; top: 150px;
    font-size: 10px; color: var(--grey);
  }
  .contact__line { display: flex; align-items: center; gap: 6px; margin-bottom: 6px; }
  .contact__item { display: inline-flex; align-items: center; gap: 5px; margin-right: 14px; }
  .icon { width: 10px; height: 10px; fill: var(--red); }
  .contact__web { color: var(--red); font-weight: 700; font-size: 11px; margin-top: 10px; }

  .footer {
    position: absolute; left: 0; right: 0; bottom: 0; height: 64px;
  }
  .footer__rule {
    position: absolute; left: 0; right: 0; top: 0; height: 4px; background: var(--ink);
  }
  .footer__band {
    position: absolute; left: 0; right: 0; top: 10px; bottom: 0;
    background: var(--red);
    display: flex; align-items: center; justify-content: center;
    color: #fff; font-weight: 700; font-size: 13px; letter-spacing: .5px;
  }
</style>
</head>
<body>

<section class="card card--front">
  <div class="brand">
    <div class="brand__row">
      <span class="brand__dot"></span>
      <span class="brand__name">NORLAND</span>
    </div>
    <div class="brand__tag">EQUITY PARTNERS</div>
  </div>
  <div class="person">
    <div class="person__name">TOM RADCLIFFE</div>
    <div class="person__title">President</div>
  </div>
  <div class="footer">
    <div class="footer__rule"></div>
    <div class="footer__band">www.NorlandEquityPartners.com</div>
  </div>
</section>

<section class="card card--back">
  <div class="brand">
    <div class="brand__row">
      <span class="brand__dot"></span>
      <span class="brand__name">NORLAND</span>
    </div>
    <div class="brand__tag">EQUITY PARTNERS</div>
  </div>
  <div class="contact">
    <div class="contact__line">
      <svg class="icon" viewBox="0 0 10 10"><path d="M5 0a3.5 3.5 0 0 0-3.5 3.5C1.5 6 5 10 5 10s3.5-4 3.5-6.5A3.5 3.5 0 0 0 5 0zm0 5a1.5 1.5 0 1 1 0-3 1.5 1.5 0 0 1 0 3z"/></svg>
      728 Maplewood Ave. Suite 310 Oak Terrace, CA 90418
    </div>
    <div class="contact__line">
      <span class="contact__item">
        <svg class="icon" viewBox="0 0 10 10"><path d="M2 0l2 2.5-1 1.2c.7 1.4 1.9 2.6 3.3 3.3l1.2-1L10 8l-1.5 2C4 10 0 6 0 1.5z"/></svg>
        (310) 555-0182
      </span>
      <span class="contact__item">
        <svg class="icon" viewBox="0 0 10 10"><path d="M0 2h10v6H0zM0 2l5 3.5L10 2" stroke="#fff" stroke-width=".8"/></svg>
        tom@NorlandEquityPartners.com
      </span>
    </div>
    <div class="contact__web">www.NorlandEquityPartners.com</div>
  </div>
  <div class="footer">
    <div class="footer__rule"></div>
    <div class="footer__band"></div>
  </div>
</section>

</body>
</html>
```